Business card design

Hi,
I need to have a business card design based on the current logo.
If competitive I not put it out to everyone.

It can be single of double sided

Target Market(s)

Food businesses

Industry/Entity Type

Food Manufacturing

Contact Information for Business Card

Details will on card will be as follows Name = Marcus Helt Email = Marcus@TalBakery.com.au Phone = 0418562207 Address = 17 Lanford Street , Fortitude Valley QLD 4006 Australia

Font styles to use
Other font styles liked:
• based on two fonts - Adelle & Museo

Requirements
Must have
• Based on the on switch concept

```html
<!DOCTYPE html>
<html lang="en">
<head>
<meta charset="utf-8">
<title>TalBakery Business Card</title>
<link rel="stylesheet" href="https://fonts.googleapis.com/css2?family=Karla:wght@400;500;700&family=Zilla+Slab:wght@400&display=swap">
<style>
  :root {
    --brand-red: #ee2a48;
    --brand-red-light: #f03d5a;
    --ink: #3c2a2d;
    --paper: #ffffff;
    --backdrop: #e4e4e4;
  }
  * { box-sizing: border-box; margin: 0; padding: 0; }
  html, body { width: 1200px; height: 1200px; overflow: hidden; }
  body {
    background: var(--backdrop);
    font-family: "Karla", sans-serif;
    position: relative;
  }
  .card {
    position: absolute;
    left: 200px;
    width: 800px;
    height: 456px;
    border-radius: 24px;
    overflow: hidden;
  }
  .card-front {
    top: 104px;
    background: linear-gradient(180deg, var(--brand-red-light) 0%, var(--brand-red) 100%);
    color: var(--paper);
  }
  .card-back {
    top: 640px;
    background: var(--paper);
  }
  .accent-circle {
    position: absolute;
    left: 366px;
    top: 31px;
    width: 394px;
    height: 394px;
  }
  .contact {
    position: absolute;
    left: 57px;
    top: 133px;
  }
  .contact-name {
    font-size: 27px;
    font-weight: 500;
    letter-spacing: 1px;
    text-transform: uppercase;
    margin-bottom: 24px;
  }
  .contact-address {
    font-style: normal;
    font-size: 17px;
    line-height: 23px;
    letter-spacing: 0.5px;
    margin-bottom: 11px;
  }
  .contact-lines { list-style: none; font-size: 17px; line-height: 22.5px; letter-spacing: 0.5px; }
  .contact-lines li { display: flex; align-items: center; gap: 10px; }
  .contact-lines svg { width: 14px; height: 14px; flex: none; }
  .brand {
    position: absolute;
    left: 0; right: 0;
    top: 176px;
    display: flex;
    justify-content: center;
  }
  .brand-lockup {
    display: flex;
    flex-direction: column;
    align-items: flex-end;
  }
  .brand-row { display: flex; align-items: center; gap: 18px; }
  .brand-dot { width: 46px; height: 46px; border-radius: 50%; background: var(--brand-red); }
  .brand-name {
    font-size: 72px;
    font-weight: 700;
    color: var(--ink);
    line-height: 1;
    letter-spacing: 1px;
  }
  .brand-tagline {
    font-family: "Zilla Slab", serif;
    font-size: 24px;
    line-height: 1;
    color: var(--ink);
    margin-top: 8px;
  }
  .web-address {
    position: absolute;
    left: 0; right: 0;
    top: 388px;
    text-align: center;
    font-size: 18px;
    letter-spacing: 4px;
    color: var(--ink);
  }
  .web-address .highlight { color: var(--brand-red); }
</style>
</head>
<body>
  <section class="card card-front">
    <svg class="accent-circle" viewBox="0 0 394 394" aria-hidden="true">
      <circle cx="197" cy="197" r="197" fill="#ffffff" fill-opacity="0.14"/>
    </svg>
    <div class="contact">
      <h1 class="contact-name">Marcus Helt</h1>
      <address class="contact-address">
        17 Lanford Street<br>
        Marlow Heights<br>
        QLD 4178 Australia
      </address>
      <ul class="contact-lines">
        <li>
          <svg viewBox="0 0 24 24" aria-hidden="true"><path fill="#fff" d="M6.6 10.8a15.1 15.1 0 0 0 6.6 6.6l2.2-2.2c.3-.3.7-.4 1-.2 1.1.4 2.3.6 3.6.6.6 0 1 .4 1 1V20c0 .6-.4 1-1 1A17 17 0 0 1 3 4c0-.6.4-1 1-1h3.5c.6 0 1 .4 1 1 0 1.3.2 2.5.6 3.6.1.3 0 .7-.2 1z"/></svg>
          0418562207
        </li>
        <li>
          <svg viewBox="0 0 24 24" aria-hidden="true"><path fill="#fff" d="M2 5h20v14H2z"/><path fill="none" stroke="#ee2a48" stroke-width="2" d="M2 5l10 8 10-8"/></svg>
          Marcus@TalBakery.com.au
        </li>
        <li>
          <svg viewBox="0 0 24 24" aria-hidden="true"><circle cx="12" cy="12" r="10" fill="#fff"/><path fill="#ee2a48" d="M8 6c2 0 3 2 2 3s-3 1-3 3 2 2 2 4-2 2-3 1a8 8 0 0 1 2-11zm7 3c2 0 4 2 3 5s-3 3-4 2 0-3-1-4 0-3 2-3z"/></svg>
          www.TalBakery.com.au
        </li>
      </ul>
    </div>
  </section>

  <section class="card card-back">
    <div class="brand">
      <div class="brand-lockup">
        <div class="brand-row">
          <span class="brand-dot" aria-hidden="true"></span>
          <span class="brand-name">TALBAKERY</span>
        </div>
        <p class="brand-tagline">Fresh Baking Made Daily</p>
      </div>
    </div>
    <p class="web-address">www.<span class="highlight">TalBakery</span>.com.au</p>
  </section>
</body>
</html>
```